"Brightwall Sound Living Residences" need a busines Card Design got Builder

We need a business card design for a company based in Milford, Michigancalled Brightwall Sound Living Residences - has been recognized as a premier custom home builder. Distinguished by outstanding craftmanship and timeless beauty. Our custom home can be found in the most prestigious communities in Michigan. The homes are built with ICF (insulated concrete homes) which is green, allergy free, fire free, mold free and quitter. Our slogan "Shaping each home with care" and also we are ICF distributor for the state of Michigan

Target Market(s)

Anyone who is making over $100,000 a year and who wants to have totally custom built home. Ages from 29 up to 60 years old

Industry/Entity Type

Concrete

Contact Information for Business Card

we want to use - green, black, gray or blue colors - we want to look different with our business cards, because we built homes only with ICF, green, healthier and highly energy efficient homes.

Requirements
Must have
• I have logo that I attached and we have been using the logo (the only green home)
Nice to have
• should look quality business card,

Files

```html
<!DOCTYPE html>
<html lang="en">
<head>
<meta charset="utf-8">
<title>Brightwall Sound Living Residences – Business Card</title>
<link rel="stylesheet" href="https://fonts.googleapis.com/css2?family=Questrial&display=swap">
<style>
  :root {
    --backdrop: #d8d3cb;
    --card: #262626;
    --card-back: #2b2b2b;
    --green: #8ed13f;
    --text-light: #c9c9c9;
    --text-mid: #a9a9a9;
    --text-dark: #1e1e1e;
    --emboss: #1c1c1c;
  }
  * { box-sizing: border-box; margin: 0; padding: 0; }
  html, body {
    width: 1200px; height: 1023px; overflow: hidden;
    background: var(--backdrop);
    font-family: "Questrial", sans-serif;
  }
  .card {
    position: absolute; left: 260px;
    width: 680px; height: 450px;
    border-radius: 18px; overflow: hidden;
    box-shadow: 0 8px 24px rgba(0,0,0,0.25);
  }
  .card--front { top: 40px; background: var(--card); }
  .card--back { top: 530px; background: var(--card-back); }

  /* front */
  .brand { position: absolute; left: 48px; top: 58px; display: flex; align-items: center; gap: 22px; }
  .brand__dot { width: 78px; height: 78px; border-radius: 50%; background: var(--green); flex: none; }
  .brand__name {
    color: var(--text-light); font-size: 30px; line-height: 1.02;
    letter-spacing: 1px; text-transform: uppercase;
  }
  .person { position: absolute; right: 48px; top: 140px; text-align: right; }
  .person__name { color: var(--green); font-size: 26px; line-height: 1.2; }
  .person__role { color: var(--text-light); font-size: 15px; line-height: 1.3; }
  .divider { position: absolute; left: 48px; right: 48px; top: 206px; height: 1px; background: var(--green); }

  .contacts { position: absolute; left: 48px; top: 270px; list-style: none; }
  .contacts li { display: flex; align-items: center; gap: 10px; color: var(--text-light); font-size: 16px; margin-bottom: 8px; }
  .contacts svg { width: 16px; height: 16px; flex: none; }

  .address { position: absolute; right: 48px; top: 264px; font-size: 15px; line-height: 1.6; color: var(--text-mid); }
  .address__company { color: var(--green); }

  .slogan-band {
    position: absolute; left: 0; right: 0; bottom: 0; height: 46px;
    background: var(--green);
    display: flex; align-items: center; justify-content: center;
    color: var(--text-dark); font-size: 19px; letter-spacing: 9px; text-transform: uppercase;
  }

  /* back */
  .back-brand {
    position: absolute; inset: 0;
    display: flex; align-items: center; justify-content: center; gap: 26px;
  }
  .back-brand__dot { width: 96px; height: 96px; border-radius: 50%; background: var(--emboss); flex: none; }
  .back-brand__name {
    color: var(--emboss); font-size: 36px; line-height: 1.02; letter-spacing: 1px;
    text-transform: uppercase;
  }
</style>
</head>
<body>
  <section class="card card--front">
    <div class="brand">
      <span class="brand__dot"></span>
      <div class="brand__name">Brightwall Sound<br>Living Residences</div>
    </div>

    <div class="person">
      <div class="person__name">Marcus Hale</div>
      <div class="person__role">President</div>
    </div>
    <div class="divider"></div>

    <ul class="contacts">
      <li>
        <svg viewBox="0 0 16 16" aria-hidden="true"><path fill="#8ed13f" d="M4 1.5l2.3 2.8-1.3 1.6c.8 1.9 2.3 3.4 4.2 4.2l1.6-1.3 2.8 2.3-1.6 2.6C6.8 13.3 2.7 9.2 1.4 3.1z"/></svg>
        555 014 2286
      </li>
      <li>
        <svg viewBox="0 0 16 16" aria-hidden="true"><rect x="1" y="3.5" width="14" height="9" fill="#8ed13f"/><path d="M1 3.5l7 5 7-5" fill="none" stroke="#262626" stroke-width="1.2"/></svg>
        info@brightwallsound.com
      </li>
      <li>
        <svg viewBox="0 0 16 16" aria-hidden="true"><circle cx="8" cy="8" r="6.5" fill="#8ed13f"/><path d="M1.5 8h13M8 1.5c-3 3.5-3 9.5 0 13M8 1.5c3 3.5 3 9.5 0 13" fill="none" stroke="#262626" stroke-width="1"/></svg>
        www.brightwallhomes.com
      </li>
    </ul>

    <div class="address">
      <div class="address__company">Brightwall Sound Living Residences</div>
      <div>P.O Box 418 Cedarline St.</div>
      <div>Harlow MI 48012</div>
    </div>

    <div class="slogan-band">Shaping each home with care</div>
  </section>

  <section class="card card--back">
    <div class="back-brand">
      <span class="back-brand__dot"></span>
      <div class="back-brand__name">Brightwall Sound<br>Living Residences</div>
    </div>
  </section>
</body>
</html>
```